Website for Painting Company

Hi,
We are after a Wordpress website design with CSS/HTML Theme for our painting company based in Brisbane, Australia. Our business name is Bevan Molloy Painting Contractors and we have been trading for 33 years.
We want a website that is modern and fresh with a professional image. Our organisation does Commercial, Residential and Insurance Painting projects. I have listed a couple of similar websites that we like the look and feel of. These are a guide only and we are happy to see you own designs with a similar professional image.
http://www.kelvardpainters.com.au/
http://www.unitedcoatworks.com.au/
We are a member of Guild Decorator Australia and I have supplied the logo named "gda" which I have included in the files I have uploaded.
We want a five page site. These are Home Page, Residential, Commercial, Insurance and Contact Us.
I have also uploaded our logo and some pictures labeled Logo,Residential, Commercial, Insurance and Homepage. These should be used on each page listed above.
Updates
Project Deadline Extended
Reason: We are extending because we need more time to go through the designs and give feedback. There are many fantastic designs. Thank you everyone who has contributed!!!!
All the best
Derek
Industry/Entity Type
Painting
Requirements
Must have
- We want a five page site. These are Home Page, Residential, Commercial, Insurance and Contact Us.

```html
<!DOCTYPE html>
<html lang="en">
<head>
<meta charset="utf-8">
<title>Contact us – Bevan Molloy and Co. Painting Contractor</title>
<link rel="stylesheet" href="https://fonts.googleapis.com/css2?family=Bree+Serif&family=Open+Sans:wght@400;600&display=swap">
<style>
  :root {
    --charcoal: #262626;
    --charcoal-deep: #1a1a1a;
    --pill: #4a4a4a;
    --green: #a8bf3a;
    --red: #b3190b;
    --red-dark: #8e1208;
    --field: #e8e8e8;
    --panel: #e9e9e9;
    --ink: #2b2b2b;
    --muted: #bdbdbd;
    --white: #ffffff;
    --orange: #f07f1e;
    --yellow: #f4c52a;
    --lime: #9fbd31;
    --sky: #1aa0dc;
    --navy: #1a4fa0;
  }
  * { box-sizing: border-box; margin: 0; padding: 0; }
  html, body { width: 1200px; height: 957px; overflow: hidden; }
  body { position: relative; background: var(--white); font-family: "Open Sans", sans-serif; color: var(--ink); }

  .site-header { position: absolute; left: 0; top: 0; width: 1200px; height: 162px; background: var(--charcoal); }
  .brand { position: absolute; left: 132px; top: 52px; display: flex; align-items: center; gap: 10px;
    font-family: "Bree Serif", serif; font-size: 20px; line-height: 24px; color: #d9d9d9; }
  .brand-mark { width: 14px; height: 14px; background: #d9d9d9; flex: none; }
  .contact-bar { position: absolute; left: 688px; top: 0; width: 393px; height: 32px; background: var(--charcoal-deep);
    border-radius: 0 0 8px 8px; font-size: 12px; color: #cfcfcf; display: flex; align-items: center; padding-left: 11px; gap: 6px; }
  .social-square { width: 20px; height: 20px; background: #3b5b9a; margin: 0 2px; }
  .main-nav { position: absolute; top: 63px; left: 498px; display: flex; font-family: "Bree Serif", serif; font-size: 16px; }
  .main-nav a { color: var(--white); text-decoration: none; padding: 7px 12px; margin-right: 33px; height: 35px; position: relative; }
  .main-nav a.current { background: var(--pill); border-radius: 6px; margin-right: 0; margin-left: 12px; }
  .main-nav a.current::after { content: ""; position: absolute; left: 40px; bottom: -7px; border: 7px solid transparent; border-bottom: 0; border-top-color: var(--pill); }

  .colour-band { position: absolute; top: 162px; left: 0; width: 1200px; height: 7px;
    background: linear-gradient(90deg, var(--orange) 0 202px, var(--yellow) 202px 523px, var(--lime) 523px 737px, var(--sky) 737px, var(--navy)); }
  .band-shade { position: absolute; top: 169px; left: 0; width: 1200px; height: 30px; background: linear-gradient(#ececec, #fff); }

  .content { position: absolute; left: 121px; top: 212px; width: 630px; }
  .content h1 { font-family: "Bree Serif", serif; font-weight: 400; font-size: 36px; line-height: 44px; color: var(--green); }
  .content p { font-size: 14px; line-height: 25px; margin-top: 1px; }
  .field { display: block; background: var(--field); border: 0; border-radius: 3px; font: 13px "Open Sans", sans-serif; color: #555; padding: 0 10px; }
  .contact-form .name { width: 260px; height: 37px; line-height: 37px; margin-top: 10px; }
  .contact-form .email { width: 260px; height: 37px; line-height: 37px; margin-top: 14px; }
  .contact-form .request { width: 628px; height: 131px; padding-top: 9px; margin-top: 14px; }
  .btn { display: inline-block; font-family: "Bree Serif", serif; color: var(--white); text-align: center;
    background: linear-gradient(var(--red), var(--red-dark)); border-radius: 3px; box-shadow: 0 1px 3px rgba(0,0,0,.4); }
  .btn-send { width: 82px; height: 37px; line-height: 38px; font-size: 14px; margin-top: 13px; }

  .panel { position: absolute; left: 777px; width: 304px; background: var(--panel); border-radius: 8px; }
  .panel-tabs { position: absolute; left: 1px; top: -11px; width: 284px; height: 11px; border-radius: 6px 6px 0 0;
    background: linear-gradient(90deg, #c7d23a 0 18%, #eee 18% 20%, #2a9ad4 20% 36%, #eee 36% 38%, #6a2b7e 38% 53%, #eee 53% 55%, #d6304a 55% 70%, #eee 70% 72%, #a0a0a0 72% 85%, #e88a3c 85%); transform: skewY(1deg); }
  .panel-pin { position: absolute; right: 10px; top: 9px; width: 10px; height: 10px; border-radius: 50%; background: #f8f8f8; border: 1px solid #c8c8c8; }
  .panel h2 { font-family: "Bree Serif", serif; font-weight: 400; font-size: 18px; color: var(--ink); position: absolute; left: 22px; }
  .newsletter { top: 233px; height: 177px; border-bottom-right-radius: 0; }
  .newsletter h2 { top: 17px; }
  .newsletter .field { position: absolute; left: 20px; width: 262px; height: 38px; line-height: 38px; background: #f7f7f7; border: 1px solid #dadada; }
  .newsletter .n1 { top: 60px; } .newsletter .n2 { top: 111px; }
  .submit-tab { position: absolute; left: 975px; top: 410px; width: 106px; height: 26px; background: var(--panel); border-radius: 0 0 8px 8px; }
  .btn-submit { position: absolute; left: 985px; top: 400px; width: 86px; height: 27px; line-height: 27px; font-size: 11px; }

  .testimonials { top: 467px; height: 300px; }
  .testimonials h2 { top: 17px; }
  .testimonial-list { position: absolute; left: 22px; top: 46px; width: 261px; list-style: none; }
  .testimonial-list li { padding: 0 0 7px; margin-bottom: 8px; border-bottom: 1px dotted #999; }
  .testimonial-list li:last-child { border: 0; }
  .client { font-family: "Bree Serif", serif; font-size: 13px; color: var(--red); line-height: 18px; }
  .quote { font-size: 12px; line-height: 20px; color: #222; }

  .site-footer { position: absolute; left: 0; top: 815px; width: 1200px; height: 142px; background: var(--charcoal); }
  .swatch-fan { position: absolute; left: 125px; top: 0; width: 955px; height: 80px; border-radius: 0 0 10px 10px;
    clip-path: polygon(0 0, 100% 0, 100% 92%, 96% 100%, 0 22%);
    background: linear-gradient(90deg, #555 0 5.5%, #e08a1e 5.5% 19.6%, #f4f4f4 19.6% 25.8%, #cc2a2a 25.8% 39.6%, #f4f4f4 39.6% 45.7%, #a8265a 45.7% 59.6%, #f4f4f4 59.6% 65.6%, #1b3f86 65.6% 79.5%, #f4f4f4 79.5% 85.6%, #8fbb32 85.6%); }
  .member-badge { position: absolute; left: 136px; top: 47px; width: 62px; height: 62px; border-radius: 50%; background: var(--white); box-shadow: 0 2px 4px rgba(0,0,0,.6); }
  .member-badge::after { content: ""; position: absolute; left: 14px; top: 14px; width: 34px; height: 34px; border-radius: 50%; background: #2f4fa3; }
  .footer-nav { position: absolute; left: 215px; top: 53px; font-size: 11.5px; color: var(--white); }
  .footer-nav a { color: var(--white); text-decoration: none; }
  .membership { position: absolute; left: 215px; top: 72px; font-family: "Bree Serif", serif; font-size: 12px; color: var(--muted); }
  .copyright { position: absolute; left: 215px; top: 90px; font-size: 12px; color: var(--muted); }
</style>
</head>
<body>
  <header class="site-header">
    <div class="brand"><span class="brand-mark"></span><span>Bevan Molloy and Co.<br>Painting Contractor</span></div>
    <div class="contact-bar">Follow us on <span class="social-square"></span> | &nbsp;PO Box 456, Brisbane, 4000 | (+61) 3000 5120</div>
    <nav class="main-nav">
      <a href="#">home</a><a href="#">residential</a><a href="#">commercial</a><a href="#">inurance</a><a href="#" class="current">contact us</a>
    </nav>
  </header>
  <div class="colour-band"></div>
  <div class="band-shade"></div>

  <main class="content">
    <h1>Contact us</h1>
    <p>Lorem ipsum dolor sit amet, consectetuer adipiscing elit. Phasellus hendrerit. Pellentesque aliquet nibh nec urna. In nisi neque, aliquet vel, dapibus id, mattis vel, nisi. Sed pretium, ligula sollicitudin laoreet viverra, tortor libero sodales leo, eget blandit nunc tortor eu nibh. Nullam mollis. Ut justo. Suspendisse potenti.</p>
    <form class="contact-form">
      <div class="field name">enter your name here...</div>
      <div class="field email">enter your e-mail address here...</div>
      <div class="field request">enter your request here...</div>
      <span class="btn btn-send">SEND</span>
    </form>
  </main>

  <aside>
    <section class="panel newsletter">
      <div class="panel-tabs"></div><div class="panel-pin"></div>
      <h2>NEWSLETTER SUBSCRIPTION</h2>
      <div class="field n1">enter your name here...</div>
      <div class="field n2">enter your e-mail address here...</div>
    </section>
    <div class="submit-tab"></div>
    <span class="btn btn-submit">SUBMIT</span>

    <section class="panel testimonials">
      <div class="panel-tabs"></div><div class="panel-pin"></div>
      <h2>TESTIMONIALS</h2>
      <ul class="testimonial-list">
        <li><div class="client">Client #1</div><div class="quote">"Lorem ipsum dolor sit amet, consectetuer adipiscing elit. Donec odio. Quisque volutpat mattis eros. Nullam malesuada erat ut turpis."</div></li>
        <li><div class="client">Client #2</div><div class="quote">"Lorem ipsum dolor sit amet, consectetuer adipiscing elit. Donec odio."</div></li>
        <li><div class="client">Client #3</div><div class="quote">"Lorem ipsum dolor sit amet, consectetuer adipiscing elit. Donec odio. Quisque volutpat mattis eros. Nullam malesuada erat ut turpis."</div></li>
      </ul>
    </section>
  </aside>

  <footer class="site-footer">
    <div class="swatch-fan" role="img" aria-label="Fanned paint colour swatch cards"></div>
    <div class="member-badge" role="img" aria-label="Member association badge"></div>
    <nav class="footer-nav"><a href="#">HOME</a> | <a href="#">RESIDENTIAL</a> | <a href="#">COMMERCIAL</a> | <a href="#">INSURANCE</a> | <a href="#">CONTACT US</a></nav>
    <div class="membership">Guild Decorator Australia - Registered member</div>
    <div class="copyright">© 2012 Bevan Molloy and Co. Painting Contractor. All rights reserved</div>
  </footer>
</body>
</html>
```